Brivet Baits Website

Brivet Baits is a start-up fishing lure company, specializing in offshore saltwater fishing lures that dive deep into the water to attract large game fish (wahoo, king mackerel, tuna, cobia, dorado).

The target market is primarily affluent outdoorsman and woman that appreciate high quality fishing equipment and spend a significant amount of time and money in their pursuits of large game fish. I would classify offshore fishing of this type as an "extreme sport", so action and boldness are good color and graphic themes for a website like this.

I have several websites in this industry that I like and would be directed at similar customers:
http://www.norvantackle.com/
http://www.quillmoor.com/quillmoor-baits/
http://www.tidelockmarine.com/
http://www.brinecove.com/

The tag line for the company is "Go Deep". I have attached the company logo in .eps format.

Navigation Menu
Home | Company | Products | What is QL-snare? | Tackle Shop | Contact Us | Media | Distributors

Scope: Landing page design & secondary page templates.
Updates

I don't have product images yet, as they are in manufacturing. I am more interested in creating a brand image, then I can add product images later and incorporate those into the page.

Target Market(s)

Affluent offshore sportsman
Distributors of fishing lures: HookVantage
Retailers of fishing lures: FinCrest, Morvins

Industry/Entity Type

Industry

Font styles to use
Serif
Sans Serif

Requirements
Must have
• Company Logo
QL-snare Logo incorporated into design - QL-snare is the key unique identifier of the lure built into the front diving lip in the image below. In addition to the company logo, this logo should be prominent on the landing page. I uploaded multiple colors to accommodate several different color selections on the landing page.

```html
<!DOCTYPE html>
<html lang="en">
<head>
<meta charset="utf-8">
<title>QL-snare — Online Market</title>
<link href="https://fonts.googleapis.com/css2?family=Open+Sans:wght@300;400;600;700&display=swap" rel="stylesheet">
<style>
:root{
  --dark:#3d414d;
  --navy:#343c4d;
  --orange:#f0522a;
  --blue:#1ba1e2;
  --crimson:#d41f46;
  --text:#333a44;
  --muted:#7b7f87;
  --line:#e3e3e3;
  --tile:#f3f3f3;
  --white:#ffffff;
}
*{box-sizing:border-box;margin:0;padding:0}
html,body{width:1200px;height:2264px;overflow:hidden;background:var(--white)}
body{position:relative;font-family:'Open Sans',Arial,sans-serif;color:var(--text)}
a{color:inherit;text-decoration:none}

/* top bar */
.topbar{position:absolute;left:0;top:0;width:1200px;height:78px;background:var(--dark);color:var(--white)}
.topbar .call{position:absolute;left:800px;top:14px;display:flex;gap:12px;align-items:flex-start}
.topbar .call .lbl{font-size:12px;font-weight:700;line-height:18px}
.topbar .call .num{font-size:12px;line-height:22px}
.topbar .sep{position:absolute;left:940px;top:0;width:1px;height:78px;background:#555a66}
.topbar .follow{position:absolute;left:954px;top:14px;font-size:12px;font-weight:700}
.topbar .socials{position:absolute;left:954px;top:35px;display:flex;gap:6px}
.topbar .socials span{width:24px;height:24px;border:2px solid #8b8f98;border-radius:50%}
.topbar .socials span.on{border-color:var(--orange)}

/* header */
.brand{position:absolute;left:100px;top:114px;font-size:32px;font-weight:700;color:var(--navy);letter-spacing:1px;display:flex;align-items:center;gap:10px;white-space:nowrap}
.brand i{display:block;width:16px;height:16px;border-radius:50%;background:var(--orange)}
.brand-rule{position:absolute;left:330px;top:118px;width:2px;height:58px;background:var(--navy)}
.tagline{position:absolute;left:347px;top:137px;font-size:12px;color:var(--text)}
.account{position:absolute;left:659px;top:118px;font-size:10px;color:var(--text);white-space:nowrap}
.cart{position:absolute;left:976px;top:107px;display:flex;align-items:center;gap:14px;font-size:11px}
.cart .badge{position:absolute;left:20px;top:-2px;width:15px;height:15px;border-radius:50%;background:var(--orange);color:#fff;font-size:9px;text-align:center;line-height:15px}
.corner{position:absolute;left:1056px;top:78px;width:46px;height:42px}
.search-band{position:absolute;left:740px;top:164px;width:362px;height:40px}
.search-box{position:absolute;left:779px;top:171px;width:302px;height:27px;border:1px solid var(--white);color:#fff;font-size:11px;padding-left:12px;line-height:25px}

/* nav */
.nav{position:absolute;left:98px;top:204px;width:1004px;height:68px;background:var(--dark)}
.nav-home{position:absolute;left:98px;top:189px;width:104px;height:83px;background:var(--orange);color:#fff;font-size:13px;font-weight:700;text-align:center;line-height:83px}
.nav ul{list-style:none;position:absolute;top:0;left:0;height:68px}
.nav li{position:absolute;top:25px;color:#fff;font-size:12px;font-weight:600;white-space:nowrap;display:flex;gap:6px;align-items:center}
.nav li svg{width:12px;height:12px}

/* hero */
.hero{position:absolute;left:0;top:272px;width:1200px;height:516px;background:linear-gradient(180deg,#3d7fb9 0%,#2f6aa5 40%,#3b78b2 70%,#6e9fcd 100%)}
.hero-arrow{position:absolute;top:483px;width:52px;height:52px;background:var(--orange)}

/* sidebar */
.cats{position:absolute;left:98px;top:838px;width:234px;height:546px;border:1px solid #cfd2d6;border-radius:5px}
.cats-head{position:absolute;left:98px;top:838px;width:234px;height:49px;background:var(--orange);border-radius:5px 5px 0 0;color:#fff;font-size:16px;font-weight:700;padding:12px 18px}
.cat{position:absolute;font-size:11px;white-space:nowrap}
.cat.folder{left:117px;font-weight:700;font-size:10px;display:flex;gap:14px;align-items:center}
.cat.folder svg{width:17px;height:14px}
.cat.sub{left:129px;color:var(--muted);font-size:12px}
.cat.sub b{display:inline-block;width:12px;font-weight:400;color:#999}
.cat.leaf{left:160px;color:var(--muted);font-size:12px}
.cat-rule{position:absolute;height:1px;background:var(--line)}
.filter-title{position:absolute;left:100px;top:1399px;font-size:13px}
.slider{position:absolute;left:103px;top:1436px;width:220px;height:12px}
.filter-btn{position:absolute;left:98px;top:1459px;width:80px;height:35px;background:var(--orange);color:#fff;font-size:12px;text-align:center;line-height:35px}
.price-range{position:absolute;left:188px;top:1468px;font-size:13px;color:var(--muted)}
.filter-rule{position:absolute;left:98px;top:1508px;width:234px;height:1px;background:var(--line)}

/* market */
.market-title{position:absolute;left:356px;top:826px;font-size:33px;font-weight:700;color:var(--navy)}
.sort{position:absolute;left:819px;top:838px;width:137px;border:1px solid #d6d6d6;background:#fff;font-size:10px}
.sort div{height:26px;line-height:26px;padding-left:10px;border-top:1px solid #e6e6e6;color:#555}
.sort div:first-child{border-top:none;color:var(--text)}
.sort div.hl{background:#f4f4f4}
.show{position:absolute;left:964px;top:838px;width:138px;height:26px;border:1px solid #d6d6d6;font-size:10px;line-height:24px;padding-left:10px}
.chev{position:absolute;right:0;top:0;width:22px;height:24px;border-left:1px solid #d6d6d6;text-align:center;font-size:9px}

.card{position:absolute;width:240px;height:354px;border:1px solid #e6e6e6;background:#fff}
.card .pic{position:absolute;left:0;top:0;width:238px;height:222px;background:var(--tile)}
.card .pic div{position:absolute;left:64px;top:58px;width:110px;height:106px;border-radius:40%;background:radial-gradient(circle,#8d8f94 0%,#c9cbcf 60%,var(--tile) 72%)}
.card .sale{position:absolute;left:179px;top:188px;width:42px;height:42px;border-radius:50%;background:var(--orange);color:#fff;font-size:12px;text-align:center;line-height:42px}
.card .title{position:absolute;left:17px;top:238px;font-size:15px;font-weight:700;color:var(--navy)}
.card .title.hot{color:var(--orange)}
.card .price{position:absolute;left:17px;top:259px;font-size:19px;color:var(--orange)}
.card .price s{font-size:13px;color:var(--muted);margin-right:8px}
.card .stars{position:absolute;right:17px;top:266px;font-size:12px;color:var(--crimson);letter-spacing:1px}
.card .rule{position:absolute;left:17px;right:17px;top:305px;height:3px;border-top:1px solid var(--line);border-bottom:1px solid var(--line)}
.card .act{position:absolute;top:325px;font-size:13px;display:flex;align-items:center;gap:8px;color:var(--text)}
.card .act.add{left:17px}
.card .act.add.hot{color:var(--orange)}
.card .act.det{right:17px}
.card .act svg{width:14px;height:13px}

.pager{position:absolute;left:830px;top:1674px;display:flex;align-items:center;gap:6px;font-size:13px}
.pager span.n{width:16px;height:15px;border:1px solid #999;font-size:9px;text-align:center;line-height:13px;color:#666}
.pager span.cur{background:var(--orange);border-color:var(--orange);color:#fff}
.pager span.mk{border-color:var(--orange);color:var(--orange)}

/* offers */
.offers-title{position:absolute;left:98px;top:1697px;font-size:24px;font-weight:300;color:var(--muted)}
.offers-title b{font-weight:400;color:var(--navy)}
.offer{position:absolute;top:1743px;height:158px;color:#fff}
.offer .ico{position:absolute;left:34px;top:52px;width:52px;height:58px}
.offer .l1{position:absolute;font-weight:400;white-space:nowrap;line-height:1.2}
.offer.blue{left:98px;width:321px;background:var(--blue)}
.offer.red{left:441px;width:320px;background:var(--crimson)}
.offer.navy{left:782px;width:321px;background:var(--navy)}

/* footer */
.foot-rule{position:absolute;left:98px;width:1004px;height:1px;background:var(--line)}
.foot-h{position:absolute;top:1964px;font-size:14px;font-weight:400;color:var(--navy)}
.about{position:absolute;left:98px;top:2002px;list-style:none;font-size:11px;color:#555}
.about li{height:25.7px;display:flex;align-items:center;gap:8px}
.about li::before{content:"+";color:#aaa;font-size:10px}
.tweet{position:absolute;left:353px;display:flex;gap:13px}
.tweet i{display:block;width:26px;height:26px;background:var(--dark);flex:none}
.tweet p{font-size:10px;line-height:15px;color:#444;width:160px}
.tweet-rule{position:absolute;left:353px;top:2080px;width:186px;height:1px;background:#999}
.photos{position:absolute;left:635px;top:2004px;width:184px;height:148px;display:grid;grid-template-columns:repeat(3,58px);grid-auto-rows:46px;gap:5px}
.news{position:absolute;left:913px;top:2002px;width:190px;font-size:10px;line-height:14px;color:#444}
.news b{display:block;color:var(--navy);margin-bottom:4px}
.news-go{position:absolute;left:1074px;top:2075px;width:28px;height:27px;background:var(--blue)}
.cards{position:absolute;left:913px;top:2116px;display:flex;gap:4px}
.cards span{width:26px;height:17px;border-radius:2px}
.bottom-links{position:absolute;left:98px;top:2222px;font-size:10px;color:#555;display:flex;gap:18px}
.copy{position:absolute;right:98px;top:2222px;font-size:10px;color:#555}
</style>
</head>
<body>

<header>
  <div class="topbar">
    <div class="call">
      <svg width="26" height="26" viewBox="0 0 26 26"><circle cx="13" cy="13" r="11" fill="none" stroke="#f0522a" stroke-width="2.5"/><text x="13" y="17" text-anchor="middle" font-size="10" font-weight="700" fill="#f0522a" font-family="Open Sans,sans-serif">24</text></svg>
      <div><div class="lbl">CALL US</div><div class="num">+00 21 5550 1987</div></div>
    </div>
    <div class="sep"></div>
    <div class="follow">FOLLOW US</div>
    <div class="socials"><span></span><span class="on"></span><span></span><span></span><span></span></div>
  </div>

  <div class="brand"><i></i>QL-SNARE</div>
  <div class="brand-rule"></div>
  <div class="tagline">Top of our brand in world</div>
  <div class="account">MY ACCOUNT &nbsp;|&nbsp; MY WISHLIST &nbsp;|&nbsp; CHECKOUT &nbsp;|&nbsp; LOGIN/REGISTER</div>
  <div class="cart">
    <svg width="28" height="24" viewBox="0 0 28 24"><path d="M1 3h5l4 13h13l3-9H8" fill="none" stroke="#3d414d" stroke-width="2.2"/><circle cx="11" cy="20" r="2" fill="#3d414d"/><circle cx="21" cy="20" r="2" fill="#3d414d"/></svg>
    <span class="badge">0</span>
    <span>CART <b>$00.00</b></span>
  </div>
  <svg class="corner" viewBox="0 0 46 42"><polygon points="0,0 46,0 46,42" fill="#f0522a"/><path d="M26 9l3 3 3-3" fill="none" stroke="#fff" stroke-width="1.4"/></svg>
  <svg class="search-band" viewBox="0 0 362 40"><polygon points="40,0 362,0 362,40 0,40" fill="#f0522a"/></svg>
  <div class="search-box">Search</div>

  <nav class="nav">
    <ul>
      <li style="left:125px"><svg viewBox="0 0 12 12"><circle cx="6" cy="3.5" r="3" fill="#fff"/><path d="M0 12a6 5 0 0 1 12 0z" fill="#fff"/></svg>COMPANY</li>
      <li style="left:237px"><svg viewBox="0 0 12 12"><rect x="1" y="2" width="9" height="9" fill="none" stroke="#fff" stroke-width="1.4"/><path d="M5 7l6-6" stroke="#fff" stroke-width="1.6"/></svg>PRODUCTS</li>
      <li style="left:355px"><svg viewBox="0 0 12 12"><polygon points="0,6 12,0 8,12 6,7" fill="#fff"/></svg>WHAT IS QL-SNARE?</li>
      <li style="left:520px"><svg viewBox="0 0 12 12"><path d="M0 1h3l2 7h6l1-5H4" fill="none" stroke="#fff" stroke-width="1.4"/><circle cx="5" cy="10.5" r="1.2" fill="#fff"/><circle cx="10" cy="10.5" r="1.2" fill="#fff"/></svg>TACKLE SHOP</li>
      <li style="left:655px"><svg viewBox="0 0 12 12"><path d="M1 11l6-6M6 2l4 4 2-2-4-4z" stroke="#fff" stroke-width="1.8" fill="#fff"/></svg>CONTACT US</li>
      <li style="left:790px"><svg viewBox="0 0 12 12"><path d="M1 11l6-6M6 2l4 4 2-2-4-4z" stroke="#fff" stroke-width="1.8" fill="#fff"/></svg>MEDIA</li>
      <li style="left:884px"><svg viewBox="0 0 12 12"><path d="M1 11l6-6M6 2l4 4 2-2-4-4z" stroke="#fff" stroke-width="1.8" fill="#fff"/></svg>DISTRIBUTORS</li>
    </ul>
  </nav>
  <div class="nav-home">&#8962; HOME</div>
</header>

<section class="hero" role="img" aria-label="Tuna leaping out of deep blue ocean water with white spray"></section>
<svg class="hero-arrow" style="left:98px" viewBox="0 0 52 52"><rect width="52" height="52" fill="#f0522a"/><path d="M30 16l-10 10 10 10" fill="none" stroke="#fff" stroke-width="3"/></svg>
<svg class="hero-arrow" style="left:1050px" viewBox="0 0 52 52"><rect width="52" height="52" fill="#f0522a"/><path d="M22 16l10 10-10 10" fill="none" stroke="#fff" stroke-width="3"/></svg>

<aside>
  <div class="cats"></div>
  <div class="cats-head">CATAGORIES</div>
  <div class="cat folder" style="top:898px"><svg viewBox="0 0 17 14"><path d="M0 1h6l2 2h9v11H0z" fill="#777"/></svg>USED F FOR CLOSED FOLDERS</div>
  <div class="cat-rule" style="left:117px;top:922px;width:196px"></div>
  <div class="cat folder" style="top:936px"><svg viewBox="0 0 17 14"><path d="M0 1h6l2 2h7v3H4L0 14z" fill="#777"/><path d="M4 7h13l-4 7H0z" fill="#777"/></svg>USED F FOR OPEN FOLDERS</div>
  <div class="cat-rule" style="left:117px;top:960px;width:196px"></div>
  <div class="cat sub" style="top:969px"><b>•</b>Lorem Ipsum Is Dummy</div>
  <div class="cat-rule" style="left:129px;top:992px;width:184px"></div>
  <div class="cat sub" style="top:998px"><b>-</b>Lorem Ipsum</div>
  <div class="cat-rule" style="left:129px;top:1021px;width:184px"></div>
  <div class="cat leaf" style="top:1028px">Just Like This</div>
  <div class="cat-rule" style="left:160px;top:1051px;width:124px"></div>
  <div class="cat leaf" style="top:1058px">Or Like This</div>
  <div class="cat-rule" style="left:129px;top:1081px;width:184px"></div>
  <div class="cat sub" style="top:1088px"><b>•</b>Lorem Ipsum Is Dummy Text</div>
  <div class="cat-rule" style="left:129px;top:1112px;width:184px"></div>
  <div class="cat sub" style="top:1118px"><b>•</b>Lorem</div>
  <div class="cat-rule" style="left:129px;top:1142px;width:184px"></div>
  <div class="cat sub" style="top:1148px"><b>-</b>Lorem Is Dummy Text</div>
  <div class="cat-rule" style="left:129px;top:1172px;width:184px"></div>
  <div class="cat leaf" style="top:1179px">Just Like This</div>
  <div class="cat-rule" style="left:160px;top:1202px;width:124px"></div>
  <div class="cat leaf" style="top:1209px">Or Like This</div>
  <div class="cat-rule" style="left:117px;top:1233px;width:196px"></div>
  <div class="cat folder" style="top:1243px"><svg viewBox="0 0 17 14"><path d="M0 1h6l2 2h9v11H0z" fill="#777"/></svg>USED F FOR CLOSED FOLDERS</div>
  <div class="cat-rule" style="left:117px;top:1270px;width:196px"></div>
  <div class="cat folder" style="top:1281px"><svg viewBox="0 0 17 14"><path d="M0 1h6l2 2h9v11H0z" fill="#777"/></svg>USED F FOR CLOSED FOLDERS</div>
  <div class="cat-rule" style="left:117px;top:1308px;width:196px"></div>
  <div class="cat folder" style="top:1320px"><svg viewBox="0 0 17 14"><path d="M0 1h6l2 2h9v11H0z" fill="#777"/></svg>USED F FOR CLOSED FOLDERS</div>
  <div class="cat-rule" style="left:117px;top:1346px;width:196px"></div>

  <div class="filter-title">QL-snare Price Filters</div>
  <svg class="slider" viewBox="0 0 220 12"><rect x="0" y="5" width="220" height="3" fill="#ccc"/><rect x="37" y="5" width="180" height="3" fill="#f0522a"/><circle cx="37" cy="6" r="5" fill="#fff" stroke="#555" stroke-width="1.5"/><circle cx="214" cy="6" r="5" fill="#fff" stroke="#555" stroke-width="1.5"/></svg>
  <div class="filter-btn">FILTER</div>
  <div class="price-range">Price: &nbsp;$25 - $85</div>
  <div class="filter-rule"></div>
</aside>

<main>
  <h1 class="market-title">Online Market</h1>
  <div class="show">Show <b>15 Products</b><span class="chev">&#9660;</span></div>

  <article class="card" style="left:358px;top:895px">
    <div class="pic" role="img" aria-label="Spinning fishing reel"><div></div></div>
    <span class="sale">Sale!</span>
    <div class="title">Product Title</div>
    <div class="price"><s>$60</s>$85.00</div>
    <div class="stars">★★★★☆</div>
    <div class="rule"></div>
    <div class="act add"><svg viewBox="0 0 14 13"><path d="M0 1h3l2 7h7l1-5H4" fill="none" stroke="currentColor" stroke-width="1.6"/><circle cx="5.5" cy="11" r="1.3" fill="currentColor"/><circle cx="11" cy="11" r="1.3" fill="currentColor"/></svg>Add To Cart</div>
    <div class="act det"><svg viewBox="0 0 14 13"><path d="M0 2h2M0 6h2M0 10h2M4 2h10M4 6h10M4 10h10" stroke="currentColor" stroke-width="2"/></svg>Details</div>
  </article>
  <article class="card" style="left:611px;top:895px">
    <div class="pic" role="img" aria-label="Light blue crankbait lure"><div></div></div>
    <div class="title">Another Product</div>
    <div class="price">$30.00</div>
    <div class="rule"></div>
    <div class="act add"><svg viewBox="0 0 14 13"><path d="M0 1h3l2 7h7l1-5H4" fill="none" stroke="currentColor" stroke-width="1.6"/><circle cx="5.5" cy="11" r="1.3" fill="currentColor"/><circle cx="11" cy="11" r="1.3" fill="currentColor"/></svg>Add To Cart</div>
    <div class="act det"><svg viewBox="0 0 14 13"><path d="M0 2h2M0 6h2M0 10h2M4 2h10M4 6h10M4 10h10" stroke="currentColor" stroke-width="2"/></svg>Details</div>
  </article>
  <article class="card" style="left:863px;top:895px">
    <div class="pic" role="img" aria-label="Silver spinning reel"><div></div></div>
    <div class="title">Yet Another Product</div>
    <div class="price">$49.95</div>
    <div class="rule"></div>
    <div class="act add hot"><svg viewBox="0 0 14 13"><path d="M0 1h3l2 7h7l1-5H4" fill="none" stroke="currentColor" stroke-width="1.6"/><circle cx="5.5" cy="11" r="1.3" fill="currentColor"/><circle cx="11" cy="11" r="1.3" fill="currentColor"/></svg>Add To Cart</div>
    <div class="act det"><svg viewBox="0 0 14 13"><path d="M0 2h2M0 6h2M0 10h2M4 2h10M4 6h10M4 10h10" stroke="currentColor" stroke-width="2"/></svg>Details</div>
  </article>

  <article class="card" style="left:358px;top:1260px">
    <div class="pic" role="img" aria-label="Yellow tackle bag with rod"><div></div></div>
    <div class="title hot">Product Title</div>
    <div class="price">$85.00</div>
    <div class="stars">★★★★☆</div>
    <div class="rule"></div>
    <div class="act add"><svg viewBox="0 0 14 13"><path d="M0 1h3l2 7h7l1-5H4" fill="none" stroke="currentColor" stroke-width="1.6"/><circle cx="5.5" cy="11" r="1.3" fill="currentColor"/><circle cx="11" cy="11" r="1.3" fill="currentColor"/></svg>Add To Cart</div>
    <div class="act det"><svg viewBox="0 0 14 13"><path d="M0 2h2M0 6h2M0 10h2M4 2h10M4 6h10M4 10h10" stroke="currentColor" stroke-width="2"/></svg>Details</div>
  </article>
  <article class="card" style="left:611px;top:1260px">
    <div class="pic" role="img" aria-label="Camouflage tackle waist pack"><div></div></div>
    <div class="title">Another Product</div>
    <div class="price">$30.00</div>
    <div class="rule"></div>
    <div class="act add"><svg viewBox="0 0 14 13"><path d="M0 1h3l2 7h7l1-5H4" fill="none" stroke="currentColor" stroke-width="1.6"/><circle cx="5.5" cy="11" r="1.3" fill="currentColor"/><circle cx="11" cy="11" r="1.3" fill="currentColor"/></svg>Add To Cart</div>
    <div class="act det"><svg viewBox="0 0 14 13"><path d="M0 2h2M0 6h2M0 10h2M4 2h10M4 6h10M4 10h10" stroke="currentColor" stroke-width="2"/></svg>Details</div>
  </article>
  <article class="card" style="left:863px;top:1260px">
    <div class="pic" role="img" aria-label="Blue fishing kayak"><div></div></div>
    <div class="title">Yet Another Product</div>
    <div class="price">$49.95</div>
    <div class="rule"></div>
    <div class="act add"><svg viewBox="0 0 14 13"><path d="M0 1h3l2 7h7l1-5H4" fill="none" stroke="currentColor" stroke-width="1.6"/><circle cx="5.5" cy="11" r="1.3" fill="currentColor"/><circle cx="11" cy="11" r="1.3" fill="currentColor"/></svg>Add To Cart</div>
    <div class="act det"><svg viewBox="0 0 14 13"><path d="M0 2h2M0 6h2M0 10h2M4 2h10M4 6h10M4 10h10" stroke="currentColor" stroke-width="2"/></svg>Details</div>
  </article>

  <div class="sort">
    <div>Sort by <b>Default Order</b> &#9662;</div>
    <div>Sort by Name</div>
    <div class="hl">Sort by Price</div>
    <div>Sort by Date</div>
    <div>Sort by Rating</div>
  </div>

  <div class="pager">
    <span>&#8249; &nbsp;Previous</span>
    <span class="n cur">1</span><span class="n">2</span><span class="n mk">3</span><span class="n">4</span><span class="n">5</span><span class="n">6</span>
    <span style="margin-left:14px">Next &#8250;</span>
  </div>
</main>

<section>
  <h2 class="offers-title"><b>Our</b> Special Offers</h2>
  <div class="offer blue">
    <svg class="ico" viewBox="0 0 52 58"><rect x="10" y="2" width="30" height="54" rx="5" fill="none" stroke="#fff" stroke-width="4"/><circle cx="25" cy="47" r="3" fill="#fff"/></svg>
    <div class="l1" style="left:92px;top:42px;font-size:26px">NEW AMAZING</div>
    <div class="l1" style="left:133px;top:78px;font-size:19px">Spring collection</div>
  </div>
  <div class="offer red">
    <svg class="ico" viewBox="0 0 52 58"><rect x="2" y="20" width="48" height="36" rx="3" fill="#fff"/><path d="M14 22V14a12 12 0 0 1 24 0v8" fill="none" stroke="#fff" stroke-width="4"/></svg>
    <div class="l1" style="left:130px;top:42px;font-size:18px">Extrasale 40% FOR</div>
    <div class="l1" style="left:102px;top:66px;font-size:26px">ALL PRODUCTS</div>
  </div>
  <div class="offer navy">
    <svg class="ico" viewBox="0 0 52 58"><path d="M4 54C4 20 24 4 50 4 50 34 34 54 4 54z" fill="#fff"/><path d="M4 54L38 18" stroke="#343c4d" stroke-width="3"/></svg>
    <div class="l1" style="left:95px;top:44px;font-size:25px">NEW COLLECTION</div>
    <div class="l1" style="left:95px;top:78px;font-size:18px">Inspired By nature</div>
  </div>
</section>

<footer>
  <div class="foot-rule" style="top:1936px"></div>
  <h3 class="foot-h" style="left:98px">About us</h3>
  <ul class="about">
    <li>Dolor sit amet</li><li>Nam cursus nunc</li><li>Fermentum</li><li>Consequat</li><li>Morbi mauris</li><li>Praesent felis</li><li>Molestie nec nibh</li>
  </ul>

  <h3 class="foot-h" style="left:353px">Twitte Feed</h3>
  <div class="tweet" style="top:2000px"><i></i><p>Lorem psum dolor conectetur adipcin fusace ipurus ticdunt http://www.harborline.com bibenuis mollis porttitor.</p></div>
  <div class="tweet-rule"></div>
  <div class="tweet" style="top:2094px"><i></i><p>Lorem psum dolor conectetur adipcin fusace ipurus ticdunt http://www.harborline.com bibenuis mollis porttitor.</p></div>

  <h3 class="foot-h" style="left:635px">Photos On Snaplane</h3>
  <div class="photos" role="img" aria-label="Grid of nine recent photo thumbnails">
    <span style="background:#e8962a"></span><span style="background:#1ba1e2"></span><span style="background:#d9d4cf"></span>
    <span style="background:#d41f46"></span><span style="background:#8d8f94"></span><span style="background:#e8433a"></span>
    <span style="background:#e23c5a"></span><span style="background:#8cc63f"></span><span style="background:#9aa36a"></span>
  </div>

  <h3 class="foot-h" style="left:911px">Newsletter</h3>
  <div class="news"><b>Sign Up for Our Newsletter:</b>Get the word out Share this page with your friends and family. Enter your email address...</div>
  <svg class="news-go" viewBox="0 0 28 27"><rect width="28" height="27" fill="#1ba1e2"/><circle cx="14" cy="13.5" r="8" fill="none" stroke="#fff" stroke-width="2"/><path d="M10 13.5h7M14 10l3.5 3.5L14 17" fill="none" stroke="#fff" stroke-width="2"/></svg>
  <div class="cards"><span style="background:#f0822a"></span><span style="background:#1f5fa8"></span><span style="background:#e8962a"></span><span style="background:#2b7ad0"></span></div>

  <div class="foot-rule" style="top:2206px"></div>
  <nav class="bottom-links"><a>About Us</a><a>Privacy Policy</a><a>Search Terms</a><a>Advanced Search</a><a>Contact Us</a></nav>
  <div class="copy">Copyright © 2014 by Norvane. All reversed.</div>
</footer>

</body>
</html>
```